Website Needs a New Look & Feel - I am Too Old and Uncool on my Own

I want some design ideas for my current site. I need a new, more modern and dynamic look and feel. The audience for the site is 90% male, 24-54 years old, and not highly educated. English is second language for about 30% of audience, so images help. 85% of visitors view on mobile. We sell trucks and trailers to this audience. . Just want something new and cool. Tired of what I have. Current site doesn't seem strong enough to match the kind of people who drive trucks for a living. Current is site is brelvon.com. Pull relevant menu and text from the site.

Target Market(s)

Truck Drivers and Trucking Company Owners (90% male).

Industry/Entity Type

Transportation - Specifically, truck and trailer sales.

Number of Pages Required

3 page

Font styles to use
Sans Serif

Colors
0054AA
0677BA
7BADD7
CADEEF
E8F1F8

Requirements
Must have
• Images of Sleeper Trucks (like on there now) and trailers. Audience is very literal, so they need to see what we sell.
Nice to have
• Images of Sleeper Trucks (like on tMy inventory pages are boring, please show me something more user-friendly and interesting. here now) and trailers.

```html
<!DOCTYPE html>
<html lang="en">
<head>
<meta charset="utf-8">
<title>Brelvon Truck &amp; Trailer</title>
<link href="https://fonts.googleapis.com/css2?family=Roboto:wght@400;500;700;900&display=swap" rel="stylesheet">
<style>
:root{
  --blue-dark:#0054AA;
  --blue:#0677BA;
  --blue-mid:#7BADD7;
  --blue-light:#CADEEF;
  --blue-pale:#E8F1F8;
  --ink:#111418;
  --text:#555b63;
  --grey-bar:#6d6e70;
  --white:#ffffff;
}
*{box-sizing:border-box;margin:0;padding:0}
html,body{width:1200px;height:4918px;overflow:hidden}
body{font-family:'Roboto',sans-serif;color:var(--ink);background:var(--white);position:relative}
section,header,footer,.topbar{position:relative;width:1200px;overflow:hidden}
.btn{position:absolute;display:flex;align-items:center;justify-content:center;gap:8px;background:var(--blue-dark);color:#fff;font-weight:700;font-size:14px;letter-spacing:.3px;text-transform:uppercase;white-space:nowrap}
.btn-outline{background:transparent;border:2px solid #fff}
.dot-arrow{width:13px;height:13px;border-radius:50%;background:#fff;display:inline-flex;align-items:center;justify-content:center}
.social{width:24px;height:24px;border-radius:50%;background:#fff;display:inline-block}

/* top bar */
.topbar{height:34px;background:var(--grey-bar);color:#fff;font-size:13px}
.topbar .contact{position:absolute;left:110px;top:0;height:34px;display:flex;align-items:center;gap:34px}
.topbar .item{display:flex;align-items:center;gap:8px;font-weight:500}
.topbar .ic{width:22px;height:22px;border-radius:50%;background:#fff;display:flex;align-items:center;justify-content:center}
.topbar .socials{position:absolute;right:110px;top:5px;display:flex;gap:8px}

/* header */
header{height:94px;background:#fff;border-bottom:1px solid #e3e6ea}
.brand{position:absolute;left:110px;top:16px;font-weight:700;color:var(--ink);line-height:1}
.brand .name{font-size:40px;letter-spacing:1px;display:block}
.brand .sub{font-size:19px;display:block;margin-top:2px}
.nav{position:absolute;left:360px;top:38px;display:flex;gap:20px;font-size:14px;font-weight:500;color:#222}
.nav .active{color:var(--blue-dark)}
.nav .marker{position:absolute;left:12px;top:-17px;width:12px;height:12px;border:2px solid #222;border-radius:50%}
.header-cta{left:895px;top:25px;width:193px;height:44px;font-size:13px}

/* hero */
.hero{height:712px}
.hero-photo{position:absolute;left:0;top:0;width:1200px;height:673px;clip-path:polygon(0 0,100% 0,100% 80.2%,50% 100%,0 80.2%);background:linear-gradient(180deg,#7fa0c4 0%,#a9bfd6 35%,#8a8f86 62%,#5f6657 100%)}
.hero-photo::after{content:"";position:absolute;inset:0;background:linear-gradient(90deg,rgba(20,30,40,.45),rgba(20,30,40,0) 55%)}
.hero-label{position:absolute;left:109px;top:148px;color:#fff;font-size:20px;font-weight:500;z-index:2}
.hero-title{position:absolute;left:108px;top:180px;color:#fff;font-size:52px;font-weight:700;line-height:54px;z-index:2}
.hero-cta{left:109px;top:349px;width:282px;height:56px;background:var(--blue-dark);z-index:2}
.hero svg{position:absolute;left:0;top:0}

/* about */
.about{height:629px}
.about-hex{position:absolute;left:110px;top:18px}
.about h2{position:absolute;left:641px;top:80px;font-size:37px;line-height:46px;font-weight:400;width:450px}
.about h2 b{font-weight:700}
.about h2 .tail{white-space:nowrap}
.about h2 .rule{display:inline-block;width:66px;height:3px;background:var(--blue-dark);vertical-align:middle;margin-left:12px}
.about .copy{position:absolute;left:641px;top:204px;width:420px;font-size:13px;line-height:24px;color:var(--text)}
.about .copy p+p{margin-top:12px}
.about-cta{left:641px;top:419px;width:172px;height:50px}

/* inventory */
.inventory{height:859px;background:var(--blue-pale)}
.section-title{position:absolute;left:0;width:1200px;text-align:center;font-size:38px;font-weight:400}
.section-title b{font-weight:700}
.section-title::after{content:"";display:block;width:66px;height:4px;background:var(--blue-dark);margin:12px auto 0}
.tabs{position:absolute;left:223px;top:168px;display:flex;gap:10px}
.tab{width:181px;height:122px;background:#fff;transform:skewX(-10deg);position:relative;box-shadow:0 2px 6px rgba(0,40,90,.08)}
.tab.active{background:var(--blue)}
.tab .inner{transform:skewX(10deg);position:absolute;inset:0;display:flex;flex-direction:column;align-items:center;justify-content:flex-end;padding-bottom:10px;font-size:17px;font-weight:700}
.tab.active .inner{color:#fff}
.tab .thumb{width:100px;height:60px;margin-bottom:12px;border-radius:2px}
.cards{position:absolute;left:110px;top:353px;display:flex;gap:24px}
.card{width:311px;height:405px;background:#fff;padding:10px;position:relative}
.card .photo{width:291px;height:238px}
.card h3{font-size:17px;font-weight:700;line-height:24px;margin-top:24px;padding-left:0}
.card .price-l{position:absolute;left:10px;top:340px;font-size:12px;color:var(--text)}
.card .price{position:absolute;left:10px;top:358px;font-size:18px;font-weight:500}
.card .details{left:160px;top:341px;width:128px;height:42px;font-size:14px;text-transform:none}
.arrow-btn{position:absolute;top:531px;width:46px;height:46px;border-radius:50%;border:2px solid #3a3f45;background:#fff;display:flex;align-items:center;justify-content:center}

/* value */
.value{height:606px}
.value svg{position:absolute;left:0;top:0}
.value .col{position:absolute;top:138px;color:#fff;text-align:center}
.value h2{font-size:30px;line-height:37px;font-weight:400}
.value h2 b{font-weight:700}
.value p{font-size:13px;line-height:22px;margin-top:26px}
.value .more{position:relative;margin:30px auto 0;width:155px;height:46px;font-size:14px}

/* blog */
.blog{height:626px}
.blog-feature{position:absolute;left:110px;top:163px;width:466px;height:398px;background:linear-gradient(180deg,#5f6873,#3b4048 60%,#22262b)}
.blog-feature .info{position:absolute;left:34px;bottom:30px;color:#fff}
.date{display:inline-block;background:var(--blue-dark);color:#fff;font-size:12px;font-weight:500;padding:6px 9px}
.blog-feature h3{font-size:17px;font-weight:700;line-height:24px;margin-top:12px;width:400px}
.blog-item{position:absolute;left:597px;width:491px;height:191px;border:1px solid #d7dde4;background:#fff}
.blog-item .thumb{position:absolute;left:0;top:0;width:232px;height:189px}
.blog-item .info{position:absolute;left:262px;top:30px;width:210px}
.blog-item h3{font-size:15px;font-weight:700;line-height:21px;margin-top:16px}
.blog-item .link{display:inline-block;margin-top:12px;font-size:13px;font-weight:700;color:var(--blue-dark);text-decoration:underline}

/* sell */
.sell{height:422px}
.sell-bg{position:absolute;inset:0;background:linear-gradient(180deg,#dfe8f1,#eef3f8);clip-path:polygon(0 26%,50% 0,100% 8%,100% 100%,0 100%)}
.sell h2{position:absolute;left:0;top:170px;width:1200px;text-align:center;font-size:38px;font-weight:400}
.sell h2 b{font-weight:700}
.sell .rule{position:absolute;left:567px;top:229px;width:66px;height:4px;background:var(--blue-dark)}
.sell-cta{left:481px;top:279px;width:238px;height:48px}

/* contact */
.contact{height:593px;background:var(--blue-dark)}
.contact svg.bg{position:absolute;left:0;top:0}
.contact h2{position:absolute;left:125px;top:95px;font-size:38px;font-weight:400;color:#fff}
.field{position:absolute;background:#fff;font-size:12px;color:#666;padding:14px 12px}
.send{left:110px;top:437px;width:171px;height:48px;background:var(--blue-mid);font-size:13px}
.contact-photo{position:absolute;left:662px;top:101px;width:454px;height:393px;background:linear-gradient(180deg,#8fc1ea 0%,#bcd9ef 45%,#8b9a5c 72%,#5f6e3a 100%)}
.frame{position:absolute;border:3px solid #fff}
.badge{position:absolute;left:636px;top:285px;width:92px;height:89px;background:#fff;display:flex;flex-direction:column;align-items:center;justify-content:center;font-weight:700;color:var(--ink);line-height:1.05;text-align:center}

/* footer */
footer{height:343px;background:#fff}
.foot-brand{position:absolute;left:122px;top:107px;font-weight:700;line-height:1;color:var(--ink)}
.foot-brand .name{font-size:60px;letter-spacing:1px;display:block}
.foot-brand .sub{font-size:29px;display:block;margin-top:2px}
.vline{position:absolute;top:45px;width:4px;height:48px;background:var(--blue-dark)}
.foot-h{position:absolute;font-size:14px;font-weight:700;letter-spacing:.3px}
.links{position:absolute;top:103px;font-size:13px;line-height:25px;color:#555}
.cinfo{position:absolute;left:826px;top:97px;font-size:14px;line-height:22px;color:#333}
.cinfo .row{display:flex;gap:10px;margin-bottom:16px}
.copyright{position:absolute;left:110px;top:292px;font-size:13px;color:#444}
.foot-social{position:absolute;left:545px;top:286px;display:flex;gap:10px}
.foot-social span{width:28px;height:28px;border-radius:50%;border:1px solid #999;display:inline-block}
.legal{position:absolute;right:112px;top:292px;font-size:13px;color:#444}
.legal i{font-style:normal;margin:0 14px}
</style>
</head>
<body>

<div class="topbar">
  <div class="contact">
    <span class="item"><span class="ic"><svg width="12" height="12" viewBox="0 0 12 12"><path d="M1 6 11 1 8 11 6 7Z" fill="#6d6e70"/></svg></span>info@brelvon.com</span>
    <span class="item"><span class="ic"><svg width="12" height="12" viewBox="0 0 12 12"><path d="M2 1h3l1 3-2 1a7 7 0 0 0 3 3l1-2 3 1v3c-5 1-10-4-9-9Z" fill="#6d6e70"/></svg></span>Toll Free 913-555-0147</span>
  </div>
  <div class="socials"><span class="social"></span><span class="social"></span></div>
</div>

<header>
  <div class="brand"><span class="name">BRELVON</span><span class="sub">Truck &amp; Trailer</span></div>
  <nav class="nav">
    <span class="marker"></span>
    <span class="active">Home</span><span>Sleepers</span><span>Reefers</span><span>Dry Vans</span><span>Cranes</span><span>Resources</span><span>Contact</span>
  </nav>
  <span class="btn header-cta">See Our Inventory</span>
</header>

<section class="hero">
  <div class="hero-photo" role="img" aria-label="White sleeper semi truck parked on a grassy lot under a blue sky"></div>
  <div class="hero-label">Brelvon Truck &amp; Trailer</div>
  <h1 class="hero-title">Buy like a fleet -<br>save thousands</h1>
  <span class="btn hero-cta">Explore Truck &amp; Trailer</span>
  <svg width="1200" height="712" viewBox="0 0 1200 712">
    <polyline points="101,568 600,669 1097,568" fill="none" stroke="#0054AA" stroke-width="14"/>
    <polygon points="600,662 628,678 628,704 600,712 572,704 572,678" fill="#fff" stroke="#d8dee6"/>
    <polyline points="593,684 600,691 607,684" fill="none" stroke="#0054AA" stroke-width="2"/>
  </svg>
</section>

<section class="about">
  <svg class="about-hex" width="456" height="520" viewBox="0 0 456 520">
    <polygon points="228,2 454,132 454,388 228,518 2,388 2,132" fill="#fff" stroke="#CADEEF" stroke-width="3"/>
    <polygon points="228,18 440,140 440,380 228,502 16,380 16,140" fill="#fff" stroke="#CADEEF" stroke-width="1"/>
    <polygon points="228,34 425,148 425,372 228,486 31,372 31,148" fill="#7d8a97" role="img" aria-label="Row of white sleeper trucks parked side by side on a dealer lot"/>
  </svg>
  <h2><b>Wholesale Reefers,</b> Dry<br><span class="tail">Vans, &amp; Sleepers<span class="rule"></span></span></h2>
  <div class="copy">
    <p>Brelvon Truck &amp; Trailer is an equipment dealership in Kansas City, offering wholesale reefers, dry vans, and sleepers at the best prices.</p>
    <p>We aren't a normal dealership, because you can buy directly from us at wholesale price and save thousands. We don't have a fancy sales lot, but we do have the lowest prices on good, clean equipment in the country.</p>
  </div>
  <span class="btn about-cta">Learn More <span class="dot-arrow"><svg width="7" height="7" viewBox="0 0 7 7"><path d="M2 1 5 3.5 2 6" fill="none" stroke="#0054AA" stroke-width="1.6"/></svg></span></span>
</section>

<section class="inventory">
  <h2 class="section-title" style="top:76px"><b>Our Truck &amp;</b> Trailer</h2>
  <div class="tabs">
    <div class="tab"><div class="inner"><span class="thumb" style="background:linear-gradient(180deg,#e9ecef,#b9c0c8)" role="img" aria-label="Reefer trailer"></span>Reefer</div></div>
    <div class="tab active"><div class="inner"><span class="thumb" style="background:linear-gradient(180deg,#dfe7ef,#9aa8b6)" role="img" aria-label="Sleeper truck"></span>Sleepers</div></div>
    <div class="tab"><div class="inner"><span class="thumb" style="background:linear-gradient(180deg,#eef0f2,#b6bcc3)" role="img" aria-label="Dry van trailer"></span>Dry Vans</div></div>
    <div class="tab"><div class="inner"><span class="thumb" style="background:linear-gradient(180deg,#e3e5e8,#7e858c)" role="img" aria-label="Mobile crane"></span>Cranes</div></div>
  </div>
  <span class="arrow-btn" style="left:32px"><svg width="14" height="20" viewBox="0 0 14 20"><path d="M11 2 3 10l8 8" fill="none" stroke="#3a3f45" stroke-width="2"/></svg></span>
  <span class="arrow-btn" style="left:1122px"><svg width="14" height="20" viewBox="0 0 14 20"><path d="M3 2l8 8-8 8" fill="none" stroke="#3a3f45" stroke-width="2"/></svg></span>
  <div class="cards">
    <div class="card"><div class="photo" style="background:linear-gradient(180deg,#c6d3df,#eef1f4 45%,#8c9096)" role="img" aria-label="White sleeper truck, front three-quarter view"></div><h3>2020 QUARROW Meridel<br>– 319,417 Miles</h3><span class="price-l">Price</span><span class="price">$63,000</span><span class="btn details">View Details</span></div>
    <div class="card"><div class="photo" style="background:linear-gradient(180deg,#b7c6d4,#9b2a33 45%,#5a5f64)" role="img" aria-label="Red sleeper truck, front view"></div><h3>2020 QUARROW Meridel<br>– 319,417 Miles</h3><span class="price-l">Price</span><span class="price">$63,000</span><span class="btn details">View Details</span></div>
    <div class="card"><div class="photo" style="background:linear-gradient(180deg,#c9d5df,#6b7077 45%,#4c5157)" role="img" aria-label="Grey sleeper truck, front three-quarter view"></div><h3>2020 QUARROW Meridel<br>– 319,417 Miles</h3><span class="price-l">Price</span><span class="price">$63,000</span><span class="btn details">View Details</span></div>
  </div>
</section>

<section class="value">
  <svg width="1200" height="606" viewBox="0 0 1200 606">
    <polygon points="0,0 600,72 600,534 0,606" fill="#0054AA"/>
    <polygon points="600,72 1200,0 1200,606 600,534" fill="#0677BA"/>
  </svg>
  <div class="col" style="left:110px;width:370px">
    <h2><b>Buying From Brelvon</b><br>Truck &amp; Trailer</h2>
    <p>When you buy from Brelvon, you are buying at a "wholesale price." In other words, you pay the same price a truck dealer pays when they buy from us. We guarantee that you won't find a better price on the same truck or trailer anywhere in the U.S.</p>
    <span class="btn btn-outline more">Learn More</span>
  </div>
  <div class="col" style="left:705px;width:370px;top:130px">
    <h2><b>How Are The Prices</b><br>So Low?</h2>
    <p>We buy huge packages of equipment, 100+ at a time, so we get a great price on what we buy.<br>We don't operate a big retail sales lot, so we don't have all that overhead cost<br>We sell at a lower profit margin, and make it up by selling a lot more equipment.</p>
    <span class="btn btn-outline more">Learn More</span>
  </div>
</section>

<section class="blog">
  <h2 class="section-title" style="top:52px"><b>Latest</b> Blog</h2>
  <div class="blog-feature" role="img" aria-label="Crane exhibit at a construction trade show">
    <div class="info"><span class="date">May 12, 2024</span><h3>The Future of the Crane Industry: Highlights from the 2023 Liftvane Expo in Las Vegas</h3></div>
  </div>
  <div class="blog-item" style="top:163px">
    <div class="thumb" style="background:linear-gradient(135deg,#9aa2aa,#4f565d)" role="img" aria-label="Auxiliary power unit mounted on a truck frame"></div>
    <div class="info"><span class="date">Jun 16, 2025</span><h3>Transform Your Trucking Experience with an APU!</h3><span class="link">LEARN MORE</span></div>
  </div>
  <div class="blog-item" style="top:370px">
    <div class="thumb" style="background:linear-gradient(180deg,#c4d3e0,#6d737a)" role="img" aria-label="Front grille of a sleeper truck"></div>
    <div class="info"><span class="date">May 11, 2024</span><h3>Why Quarrow Meridel's are the Better Choice</h3><span class="link">LEARN MORE</span></div>
  </div>
</section>

<section class="sell">
  <div class="sell-bg" role="img" aria-label="Faded view of trucks on a lot"></div>
  <h2><b>Have More Equipment</b> Than You Need?</h2>
  <span class="rule"></span>
  <span class="btn sell-cta">Sell Your Equipment <span class="dot-arrow"><svg width="7" height="7" viewBox="0 0 7 7"><path d="M2 1 5 3.5 2 6" fill="none" stroke="#0054AA" stroke-width="1.6"/></svg></span></span>
</section>

<section class="contact">
  <svg class="bg" width="1200" height="593" viewBox="0 0 1200 593">
    <polygon points="1070,0 1200,0 1200,593 735,593" fill="#7BADD7"/>
  </svg>
  <h2>Contact Us</h2>
  <div class="field" style="left:110px;top:190px;width:233px;height:45px">First Name</div>
  <div class="field" style="left:351px;top:190px;width:233px;height:45px">Last Name</div>
  <div class="field" style="left:110px;top:245px;width:233px;height:45px">Message</div>
  <div class="field" style="left:351px;top:245px;width:233px;height:45px">Phone Number</div>
  <div class="field" style="left:110px;top:303px;width:474px;height:88px">Email Address</div>
  <span class="btn send">Send Message <span class="dot-arrow"><svg width="7" height="7" viewBox="0 0 7 7"><path d="M2 1 5 3.5 2 6" fill="none" stroke="#7BADD7" stroke-width="1.6"/></svg></span></span>
  <div class="frame" style="left:650px;top:85px;width:408px;height:378px;border-right:none;border-bottom:none"></div>
  <div class="contact-photo" role="img" aria-label="Yellow mobile crane with extended boom standing in a field"></div>
  <div class="frame" style="left:1110px;top:390px;width:18px;height:120px;border-left:none;border-top:none;border-right-width:4px"></div>
  <div class="frame" style="left:700px;top:507px;width:428px;height:3px;border:none;background:#fff"></div>
  <div class="badge"><span style="font-size:19px">BRELVON</span><span style="font-size:10px">Truck &amp; Trailer</span></div>
</section>

<footer>
  <div class="foot-brand"><span class="name">BRELVON</span><span class="sub">Truck &amp; Trailer</span></div>
  <span class="vline" style="left:413px"></span>
  <span class="vline" style="left:761px"></span>
  <div class="foot-h" style="left:486px;top:55px">QUICK LINKS</div>
  <div class="links" style="left:486px">Home<br>Sleepers<br>Reefers<br>Dry Vans<br>Cranes</div>
  <div class="links" style="left:615px">Resources<br>About Us<br>Contact</div>
  <div class="foot-h" style="left:826px;top:55px">CONTACT INFO</div>
  <div class="cinfo">
    <div class="row"><svg width="16" height="20" viewBox="0 0 16 20"><path d="M8 1a6 6 0 0 1 6 6c0 5-6 12-6 12S2 12 2 7a6 6 0 0 1 6-6Z" fill="#0054AA"/><circle cx="8" cy="7" r="2.3" fill="#fff"/></svg><span>2280 W. Harbor Ln. Ste 310 Tucson,<br>AZ 85704</span></div>
    <div class="row"><svg width="18" height="14" viewBox="0 0 18 14"><rect x="1" y="1" width="16" height="12" fill="none" stroke="#0054AA" stroke-width="2"/><path d="M1 1l8 7 8-7" fill="none" stroke="#0054AA" stroke-width="2"/></svg><span>info@brelvon.com</span></div>
    <div class="row"><svg width="16" height="16" viewBox="0 0 12 12"><path d="M2 1h3l1 3-2 1a7 7 0 0 0 3 3l1-2 3 1v3c-5 1-10-4-9-9Z" fill="#0054AA"/></svg><span style="text-decoration:underline">913-555-0147</span></div>
  </div>
  <div class="copyright">© 2026 Brelvon. All Rights Reserved.</div>
  <div class="foot-social"><span></span><span></span><span></span></div>
  <div class="legal">Privacy<i>|</i>Terms<i>|</i>Disclaimer</div>
</footer>

</body>
</html>
```